Business Card Design

We service, sell & install vehicle hoists in automotive workshops & would like the colours royal blue or green incorporated into the design.

Industry/Entity Type

Automotive

Contact Information for Business Card

KLT Lifts
Equipment Sales & Service
Dale Whitcombe 0412 587 913
Gary Sutherby 0418 692 305
14 Carver Lane Brackenvale Vic 3899
email: kltlifts@mailbox.example.au

```html
<!DOCTYPE html>
<html lang="en">
<head>
<meta charset="utf-8">
<title>KLT Lifts — Business Card</title>
<link rel="stylesheet" href="https://fonts.googleapis.com/css2?family=Open+Sans:wght@300;400;700&display=swap">
<style>
  :root {
    --backdrop: #e6e6e4;
    --card: #ffffff;
    --navy: #14197e;
    --navy-dark: #0d1160;
  }
  * { margin: 0; padding: 0; box-sizing: border-box; }
  html, body {
    width: 1200px;
    height: 938px;
    overflow: hidden;
    background: var(--backdrop);
    font-family: "Open Sans", Arial, sans-serif;
    color: var(--navy);
  }
  .card {
    position: absolute;
    left: 100px;
    top: 158px;
    width: 1000px;
    height: 621px;
    background: var(--card);
  }
  .card > * { position: absolute; line-height: 1; white-space: nowrap; }
  .accent-bar { background: var(--navy-dark); }
  .accent-bar--left { left: 0; top: 0; width: 13px; height: 277px; }
  .accent-bar--right { right: 0; bottom: 0; width: 16px; height: 278px; }

  .brand-name {
    left: 59px;
    top: 46px;
    font-size: 128px;
    font-weight: 700;
    letter-spacing: -4px;
    color: var(--navy-dark);
  }
  .brand-title {
    left: 318px;
    top: 61px;
    font-size: 64px;
    font-weight: 300;
  }
  .brand-tagline {
    left: 318px;
    top: 124px;
    font-size: 36px;
    font-weight: 300;
  }
  .person-name {
    right: 62px;
    top: 354px;
    font-size: 43px;
    font-weight: 300;
    text-transform: uppercase;
  }
  .person-name strong { font-weight: 700; }
  .contact-line {
    left: 59px;
    font-size: 29px;
    font-weight: 300;
    text-transform: uppercase;
  }
  .contact-line b { font-weight: 700; }
  .contact-line--cell { top: 445px; }
  .contact-line--email { top: 485px; }
  .contact-line--address { top: 527px; }
</style>
</head>
<body>
  <article class="card">
    <div class="accent-bar accent-bar--left"></div>
    <div class="accent-bar accent-bar--right"></div>

    <div class="brand-name">KLT</div>
    <div class="brand-title">Lifts Equipment</div>
    <div class="brand-tagline">Sales &amp; Service</div>

    <div class="person-name">Dale <strong>Whitcombe</strong></div>

    <p class="contact-line contact-line--cell"><b>Cell.</b> 0412 587 913</p>
    <p class="contact-line contact-line--email"><b>Email.</b> kltlifts@mailbox.example.au</p>
    <p class="contact-line contact-line--address"><b>Address.</b> 14 Carver Lane Brackenvale Vic 3899</p>
  </article>
</body>
</html>
```